Poster / Flyer / Advertisement for Frosk Brew Chill (Unique Product!)

We’re selling alcoholic (7.5%) flavored ice for beer…for example, you might try our Lime flavor in a Valdor. We need a great ad/poster…please follow these guidelines:
USE THE PRODUCT PHOTO & KEEP IT SIMPLE!
Use the attached “action shot” of our product prominently. I prefer just the glass of beer, so turn off the layer with the beer bottle. Photoshop in a great background and KEEP IT SIMPLE - the product shot pretty much says it all. Find a great background, add the words “Your beer is getting warm”, and layer in some of our branding (see below). That’s it! Don’t make the poster too busy!
USE OUR CURRENT BRANDING
I’ve attached AI files with all of our branding. Layer in the pattern used on the packaging, our logo, and probably the “Frosk Chill” banner. Also, given that our most popular flavor is Lime in a Valdor, I would look for a background that helps express that (just a thought, it’s up to you to make it look good!).
MAKE IT VERSATILE
We need this to be versatile and easily scale up or down in size for various applications such as:
1) Large format poster for the front window of a convenience store
2) Smaller format for poster ads in bars/restaurants
3) Even smaller format for window clings that go on the glass doors of beer coolers
I also want the words for the poster to be easily changeable for the different applications:
1) Bar – I would use the tagline “Your beer is getting warm”
2) Convenience Store – I would use the line “Don’t drink warm beer…check the freezer!” or something similar. Just need it easy to change
Updates
Project Deadline Extended
Reason: Still deciding on designs. Need time to review with business partners. Thanks all!
Target Market(s)
Beer drinkers - especially those that like fruity beers like summer shandy
Industry/Entity Type
Brewery
Font styles to use
Other font styles liked:
- Use attached fonts!
Colors
Designer to choose colors to be used in the design.
Requirements
Must have
- Use the product shot and our branding...and a simple design!
Nice to have
- Want a "drinking an ice cold beer on a summer day" feel to this.

```html
<!DOCTYPE html>
<html lang="en">
<head>
<meta charset="utf-8">
<title>Frosk Brew Chill – The Fastest Way to Cool Beer Down</title>
<link rel="stylesheet" href="https://fonts.googleapis.com/css2?family=Jost:ital,wght@0,700;0,800;0,900;1,900&display=swap">
<style>
  :root {
    --red: #e8194a;
    --navy: #17497f;
    --navy-deep: #123a6a;
    --badge: #241f20;
    --ice-light: #e9f6fd;
    --ice-mid: #7fcaf0;
    --ice-deep: #1f8fd6;
    --beer-light: #f7e9a4;
    --beer-deep: #e0b623;
  }
  * { box-sizing: border-box; margin: 0; padding: 0; }
  html, body { width: 800px; height: 1200px; overflow: hidden; background: #fff; }
  .poster {
    position: relative;
    width: 800px;
    height: 1200px;
    overflow: hidden;
    font-family: "Jost", "Futura", "Helvetica Neue", Arial, sans-serif;
  }
  .ice-backdrop {
    position: absolute; inset: 0;
    background:
      radial-gradient(ellipse at 30% 40%, rgba(255,255,255,0.5), transparent 45%),
      radial-gradient(ellipse at 85% 55%, rgba(255,255,255,0.4), transparent 40%),
      radial-gradient(ellipse at 75% 90%, rgba(255,255,255,0.3), transparent 40%),
      linear-gradient(180deg, #ffffff 0%, var(--ice-light) 12%, var(--ice-mid) 42%, var(--ice-deep) 78%, var(--ice-mid) 100%);
  }
  .headline {
    position: absolute; left: 0; right: 0; top: 22px;
    text-align: center; line-height: 1;
  }
  .headline-lead {
    display: block;
    color: var(--red);
    font-size: 72px; font-weight: 900; font-style: italic;
    letter-spacing: 0.5px;
  }
  .headline-rest {
    display: block; margin-top: 2px;
    color: var(--navy);
    font-size: 53px; font-weight: 800;
    letter-spacing: 1px;
  }
  .temperature {
    position: absolute; left: 114px; top: 182px;
    color: var(--red); font-size: 46px; font-weight: 800;
  }
  .gauge-frame { position: absolute; left: 56px; top: 240px; }
  .brand-mark {
    position: absolute; left: 322px; top: 182px;
    width: 248px; height: 248px;
    display: flex; align-items: center; justify-content: center;
  }
  .brand-mark svg { position: absolute; inset: 0; }
  .brand-name {
    position: relative;
    color: var(--red); font-size: 32px; font-weight: 800;
    text-align: center; line-height: 1.1; text-transform: uppercase;
  }
  .glass-photo {
    position: absolute; left: 320px; top: 540px; width: 362px; height: 636px;
    clip-path: polygon(0 0, 100% 0, 92% 100%, 8% 100%);
    background:
      linear-gradient(180deg, rgba(255,255,255,0.9) 0%, #fff8dc 9%, var(--beer-light) 18%, #f0d25a 55%, var(--beer-deep) 100%);
  }
  .call-to-action {
    position: absolute; left: 60px; top: 744px;
    color: var(--red); font-weight: 900; line-height: 0.9;
    text-transform: uppercase;
  }
  .cta-line-1 { display: block; font-size: 74px; }
  .cta-line-2 { display: block; font-size: 94px; }
  .cta-line-3 { display: block; font-size: 134px; }
</style>
</head>
<body>
  <main class="poster">
    <div class="ice-backdrop" role="img" aria-label="Photo of crushed blue ice cubes filling the background"></div>

    <h1 class="headline">
      <span class="headline-lead">THE FASTEST WAY</span>
      <span class="headline-rest">TO COOL BEER DOWN!</span>
    </h1>

    <div class="temperature">55°F</div>

    <svg class="gauge-frame" width="250" height="980" viewBox="0 0 250 980" aria-hidden="true">
      <rect x="16" y="16" width="218" height="990" fill="none" stroke="var(--navy-deep)" stroke-width="18"/>
    </svg>

    <div class="brand-mark">
      <svg width="248" height="248" viewBox="0 0 248 248" aria-hidden="true">
        <circle cx="124" cy="124" r="122" fill="var(--badge)"/>
      </svg>
      <span class="brand-name">Frosk<br>Brew Chill</span>
    </div>

    <div class="glass-photo" role="img" aria-label="Photo of a pint glass of golden beer splashing as a lime-flavored ice wedge drops in"></div>

    <p class="call-to-action">
      <span class="cta-line-1">Check the</span>
      <span class="cta-line-2">Freezer</span>
      <span class="cta-line-3">Now!</span>
    </p>
  </main>
</body>
</html>
```